Residential Construction Design

I'd like a business card that really explains what we do in residential construction. A big name and number, while the other information can be smaller. Since the logo is made up of grays and a teal color, the background may have to stay white? Maybe a subtle gray.(sending 2 different color schemes of the logo for different background color options) I would like a card that just appears "tough" when you look at it.

Industry/Entity Type

Residential

Contact Information for Business Card

Name and logo which will be provided.(Rex Morton Construction, LLC) Rex Morton -Licensed Contractor, Certified Home Inspector. (555) 214-7730 Email: Rmorton_Construction@quellbox.example -Remodeling -Roofs - Siding -Drywall -Decks -Pole Barns -New Construction "Serving Southwest Michigan"

```html
<!DOCTYPE html>
<html lang="en">
<head>
<meta charset="utf-8">
<title>Rex Morton Construction, LLC – Business Card</title>
<link rel="stylesheet" href="https://fonts.googleapis.com/css2?family=Lato:wght@700&family=Tenor+Sans&display=swap">
<style>
  :root {
    --stage: #e9eaea;
    --card-white: #ffffff;
    --card-white-shade: #ececec;
    --teal: #45c6b2;
    --teal-deep: #3ab3a0;
    --ink: #1f2a2a;
    --ink-soft: #2c3838;
    --logo-gray: #3b3f42;
    --on-teal: #ffffff;
  }
  * { box-sizing: border-box; margin: 0; padding: 0; }
  html, body {
    width: 1200px;
    height: 1000px;
    overflow: hidden;
    background: var(--stage);
  }
  .card {
    position: absolute;
    left: 80px;
    top: 203px;
    width: 1040px;
    height: 594px;
    border-radius: 6px;
    overflow: hidden;
    box-shadow: 0 10px 30px rgba(0,0,0,0.18);
    font-family: "Tenor Sans", sans-serif;
  }
  .card__top {
    position: absolute;
    inset: 0 0 auto 0;
    height: 250px;
    background: linear-gradient(180deg, var(--card-white) 0%, var(--card-white) 55%, var(--card-white-shade) 100%);
  }
  .card__bottom {
    position: absolute;
    inset: 250px 0 0 0;
    background: linear-gradient(135deg, var(--teal) 0%, var(--teal-deep) 100%);
  }
  .brand {
    position: absolute;
    left: 150px;
    top: 70px;
    display: flex;
    align-items: center;
    gap: 28px;
  }
  .brand__mark {
    width: 96px;
    height: 96px;
    background: var(--logo-gray);
  }
  .brand__name {
    font-size: 46px;
    line-height: 1.05;
    color: var(--logo-gray);
    letter-spacing: 0.5px;
  }
  .tagline {
    position: absolute;
    right: 50px;
    top: 200px;
    font-size: 24px;
    font-style: italic;
    color: var(--teal-deep);
  }
  .contact {
    position: absolute;
    left: 60px;
    top: 40px;
    color: var(--ink);
  }
  .contact__name {
    font-family: "Lato", sans-serif;
    font-weight: 700;
    font-size: 34px;
  }
  .contact__title {
    margin-top: 6px;
    font-size: 18px;
    text-transform: uppercase;
    letter-spacing: 0.5px;
    color: var(--ink-soft);
  }
  .contact__phone {
    margin-top: 34px;
    font-size: 32px;
  }
  .contact__email {
    margin-top: 6px;
    font-size: 27px;
  }
  .services {
    position: absolute;
    right: 50px;
    top: 40px;
    list-style: none;
    text-align: right;
    color: var(--on-teal);
    font-size: 22px;
    line-height: 1.45;
    text-transform: uppercase;
    letter-spacing: 0.5px;
  }
</style>
</head>
<body>
  <article class="card">
    <header class="card__top">
      <div class="brand">
        <span class="brand__mark"></span>
        <span class="brand__name">Rex Morton<br>Construction, LLC</span>
      </div>
      <p class="tagline">"Serving Southwest Michigan"</p>
    </header>
    <section class="card__bottom">
      <div class="contact">
        <p class="contact__name">Rex Morton</p>
        <p class="contact__title">Licensed Contractor, Certified Home Inspector</p>
        <p class="contact__phone">(555) 214-7730</p>
        <p class="contact__email">Rmorton_Construction@quellbox.example</p>
      </div>
      <ul class="services">
        <li>Remodeling</li>
        <li>Roofs</li>
        <li>Siding</li>
        <li>Drywall</li>
        <li>Decks</li>
        <li>Pole Barns</li>
        <li>New Construction</li>
      </ul>
    </section>
  </article>
</body>
</html>
```